Ironfinch Steakhouse

We are changing our restaurant from a casual upmarket dining restaurant, to an upmarket steakhouse. The restaurant is located at Ironfinch Lodge, Silver Pike Alpine Resort, BC, Canada.

The A - frame Signs are 3 feet wide by 5 foot high.
Must also work as a poster size.

Target Market(s)

25 to 65's skiers, families, affluent home owners.

Industry/Entity Type

Restaurant

Colors

Designer to choose colors to be used in the design.

Requirements
Must have
• A big, juicy, flame grilled steak image.
• Located at Ironfinch lodge.
Nice to have
• Must be bold and enticing, need to convince the tired skiers that they just have to have an awesome steak for dinner.
• Should be simple, straight to the point.
• People drinking, dining, having a great dining experience.
Should not have
• bright colors

```html
<!DOCTYPE html>
<html lang="en">
<head>
<meta charset="utf-8">
<title>Ironfinch Steakhouse – A-frame Sign</title>
<link rel="stylesheet" href="https://fonts.googleapis.com/css2?family=Cinzel:wght@400;500&family=Cormorant+Garamond:wght@500&display=swap">
<style>
  :root {
    --backdrop: #808084;
    --sign-black: #000000;
    --ink-white: #ffffff;
    --flame-yellow: #ffb347;
    --flame-orange: #f0601c;
    --flame-deep: #b8320c;
    --ember-red: #5c1406;
    --steak-crust: #4a2616;
    --steak-meat: #8a5a4c;
    --bone: #cbb8a6;
    --chive: #3f8f3a;
    --bar-steel: #5d7384;
    --bar-chrome: #c9c2b0;
  }
  html, body {
    margin: 0;
    width: 1200px;
    height: 1200px;
    overflow: hidden;
    background: var(--backdrop);
  }
  .sign {
    position: absolute;
    left: 291px;
    top: 86px;
    width: 617px;
    height: 1029px;
    background: var(--sign-black);
    color: var(--ink-white);
    font-family: "Cinzel", serif;
    box-shadow: 14px 16px 22px rgba(0,0,0,0.35);
  }
  .brand-mark {
    position: absolute;
    left: 0;
    right: 0;
    top: 104px;
    text-align: center;
    font-size: 40px;
    font-weight: 400;
    letter-spacing: 6px;
  }
  .rule {
    position: absolute;
    left: 39px;
    width: 540px;
    top: 172px;
    height: 1.5px;
    background: var(--ink-white);
  }
  .title {
    position: absolute;
    left: 0;
    right: 0;
    top: 178px;
    margin: 0;
    text-align: center;
    font-weight: 400;
    font-size: 88px;
    line-height: 74px;
    letter-spacing: 1px;
  }
  .title span { display: block; }
  .hero-photo {
    position: absolute;
    left: 0;
    top: 342px;
    width: 617px;
    height: 592px;
    overflow: hidden;
    background:
      linear-gradient(180deg, #000 0%, rgba(0,0,0,0) 9%),
      radial-gradient(ellipse 58% 20% at 50% 75%, var(--steak-meat) 0%, var(--steak-crust) 55%, rgba(74,38,22,0) 100%),
      radial-gradient(ellipse 52% 5% at 48% 60%, var(--chive) 0%, rgba(63,143,58,0) 100%),
      radial-gradient(ellipse 34% 13% at 62% 90%, var(--bone) 0%, rgba(203,184,166,0) 100%),
      radial-gradient(ellipse 24% 18% at 78% 28%, var(--bar-chrome) 0%, rgba(201,194,176,0) 100%),
      radial-gradient(ellipse 34% 24% at 80% 25%, var(--bar-steel) 0%, rgba(93,115,132,0) 100%),
      radial-gradient(ellipse 18% 30% at 20% 34%, var(--flame-yellow) 0%, rgba(255,179,71,0) 100%),
      radial-gradient(ellipse 14% 26% at 44% 42%, var(--flame-yellow) 0%, rgba(255,179,71,0) 100%),
      radial-gradient(ellipse 30% 40% at 25% 38%, var(--flame-orange) 0%, rgba(240,96,28,0) 100%),
      radial-gradient(ellipse 26% 30% at 50% 46%, var(--flame-orange) 0%, rgba(240,96,28,0) 100%),
      radial-gradient(ellipse 36% 12% at 80% 55%, var(--flame-deep) 0%, rgba(184,50,12,0) 100%),
      radial-gradient(ellipse 12% 10% at 94% 84%, var(--flame-orange) 0%, rgba(240,96,28,0) 100%),
      linear-gradient(180deg, var(--ember-red) 0%, #2a0a04 60%, #0a0403 100%);
  }
  .footer-band {
    position: absolute;
    left: 0;
    right: 0;
    top: 934px;
    height: 95px;
    display: flex;
    align-items: center;
    justify-content: center;
    font-size: 52px;
    white-space: nowrap;
  }
  .footer-band .lead {
    font-family: "Cormorant Garamond", serif;
    font-weight: 500;
    font-size: 50px;
    margin-right: 14px;
  }
</style>
</head>
<body>
  <div class="sign">
    <div class="brand-mark">Ironfinch</div>
    <div class="rule"></div>
    <h1 class="title">
      <span>Ironfinch</span>
      <span>Steakhouse</span>
    </h1>
    <div class="hero-photo" role="img" aria-label="Big flame-grilled rack of ribs, peppered and topped with chives, in front of roaring orange flames, with chrome beer taps glowing at the bar in the upper right"></div>
    <div class="footer-band"><span class="lead">at</span>Ironfinch Lodge</div>
  </div>
</body>
</html>
```